Brindle Outcomes WebDesign

Although the designs we have had are great we are looking for something unique and would like to move away from the traditional. We append additional comments and files to reflect this. WE are looking for designs to showcase there artistic flare.

Task
To design Brindle Outcomes home page and a second page ie information on our Internet Marketing Services

Client:
Brindle Outcomes is the next generation provider of international marketing, branding, design, Search Engine Optimization(SEO) and Search Engine Marketing(SEM). Utilising a variety of crowd-source channels and trust networks, Brindle Outcomes is able to offer you a complete internet marketing package. From initial design and branding to the continued work on SEO all our services are geared towards dramatically increasings your revenues. Our primary goal is to build greater trading bridges between English-speaking and Chinese-speaking worlds. We believe that a true understanding of the local market is only achievable if you are a native speaker. The power of our networks and processes have been focused to enable Brindle Outcomes to enlist only native speakers to bolster your Internet Marketing Campaign.

The primary color pallet is:

FF9571
B23308
FF6633
858585
BDBDBD
or
https://palettes.vormix.example/#themes/search?term=brindle%20outcomes

Sites we like
http://www.trevonix.example/
http://www.morbela.example/
Updates

We have believe that we will need to push our design packages (outsourced through artflockly) more. We would like this to be reflected on the front page.

This means that the menu should also include

Design
Also the use of content management system wendix

Have added a few more sites that we like
www.harbourpixelstudio.example.hk
www.qmt.example.hk

Really excited with all the designs so far.  We would like the design to move away from the more standard layout. With this in mind we would like to see some design that feature hexagons, or decagons.
Please feel free to let loose! we want a design that is quit unique

We have included to vector files.

vector file 8016151 is for a color reference we thik that in order to enhence the design we need to expand the color palette, would want to maintain the primary corporate colors, but include some bright additional colors.

The second was our insipration for the the hexagon. expanding on the idea we thought that the main menu could be made up of hexagons. The ad/info modules that appear half way up the page be similar to those in the vector.

Reason: Have updated brief and are looking for a more unique feel to the design.

Target Market(s)

Small to medium business looking to branch out further in the international market

Industry/Entity Type

Internet

Requirements
Must have
• A login/search section
A separate floating feedback tab
Main Navigation – Home, Internet Marketing, Cloud Computing
A banner space from informative text on our services
Must have a request for a quote on each page

```html
<!DOCTYPE html>
<html lang="en">
<head>
<meta charset="utf-8">
<title>Brindle Outcomes – SEO and Cloud Consultant</title>
<link rel="stylesheet" href="https://fonts.googleapis.com/css2?family=Libre+Franklin:wght@400;600;700;800&family=Anton&family=Open+Sans:wght@400;600&display=swap">
<style>
  :root{
    --orange:#ff5500;
    --orange-light:#ff9571;
    --orange-mid:#ff6633;
    --rust:#b23308;
    --red:#e8361a;
    --text-orange:#ff5a14;
    --grey:#bdbdbd;
    --grey-dark:#858585;
    --panel:#e4e4e4;
    --hero:#232323;
    --footer:#3a3a3a;
  }
  *{box-sizing:border-box;margin:0;padding:0}
  html,body{width:1200px;height:1000px;overflow:hidden}
  body{
    position:relative;
    font-family:"Libre Franklin",Arial,sans-serif;
    background:linear-gradient(90deg,#dcdcdc 0,#fff 9%,#fff 91%,#dcdcdc 100%);
  }
  .brand{position:absolute;left:90px;top:15px;width:450px;height:100px;background:#fff}
  .brand-mark{position:absolute;left:16px;top:14px;width:74px;height:74px;border:7px solid var(--orange-mid);border-radius:50%}
  .brand-name{position:absolute;left:120px;top:18px;font-family:"Open Sans",Arial,sans-serif;font-weight:600;font-size:37px;letter-spacing:-1px;color:var(--orange-mid)}
  .brand-tag{position:absolute;left:156px;top:66px;font-family:"Open Sans",Arial,sans-serif;font-size:12.5px;color:#222}
  .account{position:absolute;top:19px;left:926px;font-size:13px;font-weight:700;color:#999;display:flex}
  .account span{padding:0 12px}
  .account span:first-child{padding-left:0;border-right:1px solid #ccc}
  .backdrop{position:absolute;left:0;top:0}
  .nav{position:absolute;left:138px;top:139px;width:912px;height:38px;background:linear-gradient(#f06a1c,#c43c08);display:flex;border-bottom:1px solid #8a2a05}
  .nav-item{width:130px;height:38px;border-right:1px solid #a23205;color:#fff;font-weight:700;font-size:16px;line-height:16px;text-align:center;display:flex;align-items:center;justify-content:center;text-shadow:0 1px 1px rgba(0,0,0,.4)}
  .nav-item.mail{width:72px}
  .feedback{position:absolute;left:730px;top:110px;width:82px;height:32px;background:linear-gradient(#ff8a3a,#e95a12);border-radius:6px 6px 0 0;font-size:14px;font-weight:700;color:#222;text-align:center;padding-top:7px}
  .search-icon{position:absolute;left:776px;top:146px}
  .search-field{position:absolute;left:811px;top:145px;width:205px;height:27px;background:#e6e6e6;border:1px solid #bbb;color:#aaa;font-size:16px;padding:3px 8px}
  .search-go{position:absolute;left:1019px;top:145px;width:27px;height:27px;border-radius:50%;background:radial-gradient(circle at 40% 35%,#e05a2a,#8a2205);color:#fff;font-size:9px;font-weight:800;text-align:center;line-height:27px}
  .package-art{position:absolute;left:155px;top:268px;width:150px;height:110px;background:linear-gradient(135deg,#ffc877 0,#ff9c57 50%,#e8361a 100%)}
  .package-title{position:absolute;left:265px;top:192px;font-family:Anton,Impact,sans-serif;color:var(--red);font-size:66px;line-height:64px;letter-spacing:-1px;text-shadow:1px 2px 2px rgba(0,0,0,.5)}
  .package-title .second{display:block;padding-left:62px}
  .btn{position:absolute;background:linear-gradient(#ff8a3a,#f05a12);color:#fff;font-weight:700;font-size:16px;text-align:center;border:1px solid #c94a10;text-shadow:0 1px 1px rgba(0,0,0,.35)}
  .btn.hero-btn{left:429px;top:341px;width:95px;height:35px;line-height:33px}
  .btn.seo-btn{left:375px;top:772px;width:95px;height:34px;line-height:32px}
  .emblem{position:absolute;left:538px;top:402px;width:75px;height:75px;border:5px solid #c42a12;border-radius:50%}
  .intro{position:absolute;left:635px;top:389px;width:410px;color:var(--text-orange);font-weight:700;font-size:17px;line-height:26px;text-shadow:1px 1px 2px #000}
  .seo{position:absolute;left:179px;top:440px;width:298px;height:374px;background:var(--panel);border:1px solid #fff;box-shadow:0 0 3px rgba(0,0,0,.35);padding:12px 10px 0 13px}
  .seo h2{color:var(--red);font-size:19px;font-weight:700;text-align:center;margin-bottom:12px}
  .seo p{color:var(--text-orange);font-weight:600;font-size:15.4px;line-height:26.2px}
  .footer{position:absolute;left:138px;top:972px;width:912px;height:28px;background:var(--footer);color:#fff;font-size:12px;font-weight:700;padding:6px 18px}
</style>
</head>
<body>
  <header class="brand">
    <div class="brand-mark"></div>
    <div class="brand-name">BrindleOutcomes.com</div>
    <div class="brand-tag">SEO and Cloud Consultant</div>
  </header>
  <div class="account"><span>Login</span><span>Sign Up</span></div>

  <svg class="backdrop" width="1200" height="1000" viewBox="0 0 1200 1000">
    <rect x="138" y="177" width="912" height="395" fill="var(--hero)"/>
    <path d="M138 177 H1050 V215 Q600 175 138 260 Z" fill="#454545"/>
    <path d="M146 520 H545 L620 590 H1041 V925 H622 L557 860 H146 Z" fill="var(--orange)"/>
    <path d="M138 503 H558 L622 567 H1050 V592 H612 L545 522 H138 Z" fill="var(--grey)"/>
    <path d="M138 860 H557 L622 925 H1050 V972 H138 Z" fill="var(--grey)"/>
    <path d="M330 325 Q480 312 636 323 Q480 318 330 325 Z" fill="var(--red)" stroke="var(--red)" stroke-width="2"/>
  </svg>

  <nav class="nav">
    <div class="nav-item">Home</div>
    <div class="nav-item">Internet<br>Marketing</div>
    <div class="nav-item">Cloud<br>Computing</div>
    <div class="nav-item">Design</div>
    <div class="nav-item mail">
      <svg width="22" height="15" viewBox="0 0 22 15"><rect x="1" y="1" width="20" height="13" fill="none" stroke="#fff" stroke-width="1.5"/><path d="M1 1 L11 9 L21 1 M1 14 L8 7 M21 14 L14 7" fill="none" stroke="#fff" stroke-width="1.5"/></svg>
    </div>
  </nav>
  <div class="feedback">Feedback</div>
  <svg class="search-icon" width="26" height="26" viewBox="0 0 26 26"><circle cx="15" cy="10" r="7" fill="none" stroke="#fff" stroke-width="3"/><path d="M10 15 L3 22" stroke="#fff" stroke-width="4" stroke-linecap="round"/></svg>
  <div class="search-field">...Search</div>
  <div class="search-go">GO!</div>

  <div class="package-art" role="img" aria-label="Illustration of an open gift box"></div>
  <div class="package-title">Design<span class="second">Packages</span></div>
  <div class="btn hero-btn">Learn More</div>

  <div class="emblem"></div>
  <p class="intro">Brindle Outcomes is the next generation provider of international marketing, branding, design, Search Engine Optimization(SEO) and Search Engine Marketing(SEM).</p>

  <section class="seo">
    <h2>Search Engine Optimization</h2>
    <p>Search engine optimization (SEO) is the process of affecting the visibility of a website or a web page in a search engine's "natural" or un-paid ("organic") search results.<br>In general, the earlier (or higher ranked on the search results page), and more frequently a site appears in the search results list, the more visitors it will receive from the search engine's users.</p>
  </section>
  <div class="btn seo-btn">Learn More</div>

  <footer class="footer">© Copyright BrindleOutcomes. All rights reserved.</footer>
</body>
</html>
```